Eye-Catching, Direct Marketing Residential Painting Flyer!

I am run a residential painting business and am looking for a flyer to be designed to mailout to potential customers.
I want the copy/wording to be designed similar to this flyer.

It's important that the person reading the flyer gets the benefits we're promoting which is why I want the wording/copy to be almost identical to the flyer attached.

However, the structure will be different. The flyer will be a postcard thick, 5 x11.5.
Double sided.

The name of the company is Brightwall Coaters.

I would also like the prominent colour to either be light green or orange.

Target Market(s)

Home Owners between the age of 45-80.

Industry/Entity Type

Painting And Decorating

Font styles to use
Serif

Colors
f68d4d
faa54b
f78f20
f37122
9bcb3c
abd037
cadf82

Requirements
Must have
• Excellent Eye-Catching Design
• Benefits Visibly Promoted
• Action Taking Incentive- Call Now for FREE Window Cleaning and FREE Painting Estimate
Should not have
• Crowded wording

```html
<!DOCTYPE html>
<html lang="en">
<head>
<meta charset="utf-8">
<title>Brightwall Coaters – Exterior Painting Flyer</title>
<link href="https://fonts.googleapis.com/css2?family=Fira+Sans+Condensed:wght@600;700&family=Lato:wght@400;700&display=swap" rel="stylesheet">
<style>
  :root {
    --orange: #f37122;
    --orange-light: #faa54b;
    --orange-soft: #fbc58a;
    --ink: #1f1f1f;
    --panel-light: #ffffff;
    --panel-grey: #dcdcdc;
    --stage: #ececec;
  }
  * { box-sizing: border-box; margin: 0; padding: 0; }
  html, body { width: 1200px; height: 1200px; overflow: hidden; }
  body {
    background: var(--stage);
    font-family: "Lato", sans-serif;
    color: var(--ink);
    position: relative;
  }
  .flyer {
    position: absolute;
    left: 52px; top: 352px;
    width: 1096px; height: 496px;
    background: linear-gradient(90deg, var(--panel-grey) 0%, var(--panel-light) 20%, var(--panel-grey) 42%, var(--panel-light) 55%, var(--panel-light) 62%, var(--panel-grey) 67%);
    overflow: hidden;
  }
  .footer-bar {
    position: absolute; left: 0; bottom: 0;
    width: 100%; height: 26px; background: var(--ink);
  }
  .tag {
    position: absolute; left: 0;
    background: var(--orange);
    color: #fff;
    font-family: "Fira Sans Condensed", sans-serif;
    font-weight: 700;
    clip-path: polygon(0 0, 100% 0, 84% 100%, 0 100%);
    display: flex; align-items: center;
  }
  .tag--large { width: 158px; height: 35px; font-size: 29px; padding-left: 29px; }
  .tag--problem { top: 26px; }
  .tag--solution { top: 304px; }
  .tag--small { top: 402px; width: 141px; height: 23px; font-size: 17px; padding-left: 26px; letter-spacing: .2px; }
  .text-box {
    position: absolute;
    border: 2px solid var(--orange);
    background: #fff;
    font-size: 11.2px;
    line-height: 1.25;
    padding: 6px 5px;
  }
  .box-problem { left: 24px; top: 67px; width: 338px; height: 47px; }
  .box-solution { left: 24px; top: 345px; width: 338px; height: 47px; padding-top: 8px; }
  .testimonial {
    position: absolute; left: 24px; top: 430px; width: 330px;
    font-size: 11.4px; line-height: 1.27;
  }
  .photo-circle {
    position: absolute; border-radius: 50%;
    border: 3px solid var(--orange);
  }
  .photo-deck {
    left: 105px; top: 126px; width: 160px; height: 160px;
    background: radial-gradient(circle at 60% 40%, #a4603a, #8a6a4a 55%, #5b4a3a);
    box-shadow: inset 0 0 0 4px #fff;
  }
  .photo-team {
    left: 450px; top: 30px; width: 196px; height: 196px;
    background: linear-gradient(180deg, #4f6b3a 0%, #7d8a85 45%, #c9c9c9 100%);
    box-shadow: inset 0 0 0 5px #fff;
  }
  .offer-title {
    position: absolute; left: 400px; top: 238px; width: 296px;
    text-align: center;
    font-family: "Fira Sans Condensed", sans-serif; font-weight: 700;
    font-size: 33px; color: var(--orange); line-height: 1;
  }
  .offer-title span { border-bottom: 1px solid #999; padding-bottom: 2px; }
  .box-offer-one { left: 382px; top: 288px; width: 328px; height: 44px; font-size: 10.2px; padding: 8px 4px; }
  .box-offer-two { left: 382px; top: 342px; width: 328px; height: 50px; font-size: 10.2px; padding: 4px 4px; line-height: 1.25; }
  .estimate-label {
    position: absolute; left: 400px; top: 396px; width: 296px; text-align: center;
    font-family: "Fira Sans Condensed", sans-serif; font-weight: 600; font-size: 21px; line-height: 24px;
  }
  .estimate-phone {
    position: absolute; left: 400px; top: 418px; width: 296px; text-align: center;
    font-family: "Fira Sans Condensed", sans-serif; font-weight: 700; font-size: 33px; line-height: 38px;
    color: var(--orange);
  }
  .cover {
    position: absolute; left: 730px; top: 0; width: 366px; height: 470px;
  }
  .cover-photo {
    position: absolute; left: 0; top: 0; width: 366px; height: 307px;
    background: linear-gradient(180deg, #9a9fa6 0%, #8a8c8f 35%, #6f8a4a 60%, #3f6a2a 100%);
  }
  .cover-band {
    position: absolute; left: 0; top: 307px; width: 366px; height: 163px;
    background: linear-gradient(180deg, var(--orange-light) 0%, var(--orange-soft) 60%, var(--orange-light) 100%);
    border-top: 11px solid var(--orange);
  }
  .brand-name {
    position: absolute; left: 0; top: 318px; width: 366px; text-align: center;
    font-family: "Fira Sans Condensed", sans-serif; font-weight: 700;
    font-size: 18px; line-height: 20px; color: var(--ink);
  }
  .cover-headline {
    position: absolute; left: 0; top: 340px; width: 366px; text-align: center;
    font-family: "Fira Sans Condensed", sans-serif; font-weight: 700;
    font-size: 31px; line-height: 40px; color: #fff;
  }
  .cover-headline .dark { color: var(--ink); }
</style>
</head>
<body>
  <main class="flyer">
    <section class="panel-problem">
      <div class="tag tag--large tag--problem">Problem:</div>
      <p class="text-box box-problem">Your exterior semi-transparent deck,fence or siding is peeling, chipping or faded.</p>
      <div class="photo-circle photo-deck" role="img" aria-label="Photo of a half-stained wooden deck with a stain can and brush"></div>
      <div class="tag tag--large tag--solution">Solution:</div>
      <p class="text-box box-solution">A fresh coat of stain to protect the wood and make it look clean, fresh and beautiful!</p>
      <div class="tag tag--small">TESTIMONIAL</div>
      <p class="testimonial">“They provided us with the satisfaction that we chose wisely when we decided to grant the project to this company”</p>
    </section>

    <section class="panel-offer">
      <div class="photo-circle photo-team" role="img" aria-label="Photo of the painting crew standing together in paint-splattered shirts"></div>
      <h2 class="offer-title"><span>SPECIAL OFFER!</span></h2>
      <p class="text-box box-offer-one">If you are one of the first 17 exterior projects that book with us, you will receive a complimentary window cleaning!</p>
      <p class="text-box box-offer-two">If you are one of the first 13 exterior projects that book with us, you will receive a complimentary interior design consultation by aprofes-sional interior designer!</p>
      <p class="estimate-label">Free Estimates:</p>
      <p class="estimate-phone">647-555-0142</p>
    </section>

    <section class="cover">
      <div class="cover-photo" role="img" aria-label="Photo of a freshly painted stone house with dormers and a flowering front garden"></div>
      <div class="cover-band"></div>
      <p class="brand-name">Brightwall Coaters</p>
      <h1 class="cover-headline">We make your home look<br><span class="dark">CLEAN, FRESH &amp; Beautiful</span><br>Again!</h1>
    </section>

    <div class="footer-bar"></div>
  </main>
</body>
</html>
```